Flyer-Design für Weiterbildung von Betriebsräten und Arbeitgebern durch Seminare
Zielgruppe
Wir verbessern die Zusammenarbeit von Betriebsräten und Arbeitgebern. Die Arbeit als oder mit dem Betriebsrat soll Unternehmen weiterbringen und nicht behindern.
Dies erreichen wir, indem wir Betriebsräte und Arbeitgeber gemeinsam in Seminaren weiterbilden. So lernen beide Seiten wichtiges über den Betriebsrat. Vor allem aber lernen die Teilnehmer sich vielmehr als Partner, statt als Gegner zu sehen. So verhindert man Missverständnisse und teure Streitigkeiten.
Wir veranstalten (Rechts-) Seminare zum Arbeitsrecht und Betriebsverfassungsgesetz. Der Fokus liegt neben didaktischer Wissensvermittlung auf der Förderung der Zusammenarbeit.
Außerdem veranstalten wir Workshops. Hier liegt der Fokus nicht auf dem Lernen, sondern auf dem Lösen von Problemen. Es wird dabei individuell auf die Herausforderungen einzelner Betriebsräte eingegangen.
Unsere Zielgruppe sind Betriebsräte und Arbeitgeber, die an Lösungen interessiert sind. Fokus sind Unternehmen mit mindestens 200 Mitarbeitern.
Aufgabenstellung
Wir möchten gerne einen Flyer für den Erstkontakt, aus dem unser Ansatz der gemeinsamen Weiterbildung und unser Angebot deutlich wird. Bitte orientieren Sie sich an unserer Website www.voran-kolleg.example
Format: Beidseitig; DIN A5 oder DIN lang
Es sollte bitte der Spruch „Gemeinsam mehr erreichen“ untergebracht werden.
Farblich bitte das Blau unserer Website einarbeiten (#002147)

```html
<!DOCTYPE html>
<html lang="de">
<head>
<meta charset="utf-8">
<title>VORAN Flyer</title>
<link href="https://fonts.googleapis.com/css2?family=Roboto:wght@400;500;700;900&display=swap" rel="stylesheet">
<style>
:root{
  --navy:#1b2748;
  --red:#d9141b;
  --black:#111111;
  --text:#1f2230;
  --rule:#9a9ca3;
  --paper:#ffffff;
  --bg:#ffffff;
}
*{margin:0;padding:0;box-sizing:border-box}
html,body{width:1200px;height:1063px;overflow:hidden;background:var(--bg)}
body{position:relative;font-family:'Roboto',Arial,sans-serif;color:var(--text)}
.flyer{position:absolute;width:651px;height:459px;background:var(--paper);overflow:hidden;outline:1px solid #e6e6e6}
.flyer--front{left:72px;top:46px}
.flyer--back{left:446px;top:549px}
.abs{position:absolute}
.layer{position:absolute;left:0;top:0}
.accent{color:var(--red);font-weight:700}
.copy{font-size:9.4px;line-height:13.1px;letter-spacing:-.1px;hyphens:auto;-webkit-hyphens:auto}
.copy p+p{margin-top:6px}

/* front */
.front-title{left:243px;top:20px;font-weight:900;font-size:41px;line-height:35px;color:var(--navy);letter-spacing:-.3px}
.front-sub{left:245px;top:94px;font-size:14.2px;color:var(--text)}
.intro{left:273px;top:126px;width:352px}
.intro p{margin:0}
.intro .intro-2{margin:9px 0 0 15px}
.intro .intro-3{margin:9px 0 0 3px;text-align:justify}
.benefit{position:absolute;top:274px;width:100px;margin-left:-50px;text-align:center;color:#fff}
.benefit svg{display:block;margin:0 auto 5px}
.benefit span{display:block;font-weight:700;font-size:9.2px;line-height:10px}
.closing{left:184px;top:360px;width:438px;text-align:justify}
.rule{position:absolute;height:1px;background:var(--rule)}
.cta{left:134px;top:426px;font-size:14.2px}
.cta b{color:var(--red);font-weight:700}
.wordmark{font-weight:700;color:var(--navy);letter-spacing:.8px;display:flex;align-items:center;gap:4px}
.wordmark i{display:inline-block;background:var(--navy)}
.front-mark{right:30px;top:427px;font-size:13px}
.front-mark i{width:11px;height:11px}

/* back */
.back-title{left:26px;top:31px;font-weight:900;font-size:27.5px;line-height:28px;color:var(--navy);letter-spacing:-.2px}
.back-title em{display:block;font-style:normal;color:var(--red);font-weight:700}
.back-p1{left:26px;top:105px;width:406px}
.back-p2{left:26px;top:138px;width:406px}
.feature{position:absolute;left:0}
.feature .marker{position:absolute;left:0;top:0}
.feature h3{position:absolute;top:-3px;font-weight:900;font-size:16px;color:var(--navy);white-space:nowrap}
.feature p{position:absolute;top:15px;font-size:9.4px;white-space:nowrap}
.back-p3{left:26px;top:326px;width:464px;text-align:justify}
.back-p4{left:26px;top:372px;width:464px;text-align:justify}
.footer{left:23px;top:430px;display:flex;align-items:center;gap:9px;white-space:nowrap}
.footer .wordmark{font-size:10.5px}
.footer .wordmark i{width:9px;height:9px}
.footer small{font-size:6.9px;color:var(--text)}
.footer small b{font-weight:700}
</style>
</head>
<body>

<section class="flyer flyer--front">
  <svg class="layer" width="651" height="459" role="img" aria-label="Foto: Team im hellen Büro im Gespräch">
    <defs>
      <linearGradient id="officeTone" x1="0" y1="0" x2="1" y2="1">
        <stop offset="0" stop-color="#e9ebed"/>
        <stop offset=".5" stop-color="#a9a8a4"/>
        <stop offset="1" stop-color="#5e5e60"/>
      </linearGradient>
    </defs>
    <polygon points="0,0 152,0 265,192 78,459 0,459" fill="url(#officeTone)"/>
  </svg>
  <svg class="layer" width="651" height="459" aria-hidden="true">
    <polygon points="244,261 651,261 651,345 191,345" fill="var(--navy)"/>
    <polyline points="155,0 268,192 82,459" fill="none" stroke="var(--black)" stroke-width="4"/>
    <polyline points="164,0 277,192 92,459" fill="none" stroke="var(--red)" stroke-width="5"/>
  </svg>

  <h1 class="abs front-title">GEMEINSAM<br>MEHR ERREICHEN</h1>
  <p class="abs front-sub">Zusammen mit VORAN zur besten Betriebsratsarbeit</p>

  <div class="abs copy intro">
    <p class="intro-1">Das Voran Kolleg wurde gegründet um Unternehmen dabei zu unterstützen,<br>ihre Ziele zu erreichen.</p>
    <p class="intro-2">Damit auch Sie Ihre Ziele erreichen, muss Ihr Unternehmen als Einheit funktionieren. <span class="accent">Alle Mitarbeiter müssen mit der Unternehmensführung gemeinsam die Ziele des Unternehmens verfolgen – niemals nur jeder seine eigenen.</span></p>
    <p class="intro-3">Beim Erreichen dieser notwendigen Einigkeit ist der Betriebsrat ein starkes Instrument. Dabei kann er seine Aufgabe nur erfüllen, wenn er diesen beiden Bestimmungen gleichmäßig gerecht wird.</p>
  </div>

  <div class="benefit" style="left:287px">
    <svg width="44" height="32" viewBox="0 0 44 32" fill="none" stroke="#fff" stroke-width="1.3"><circle cx="8" cy="5" r="3"/><path d="M3 30V14l5-4 5 4v16"/><circle cx="36" cy="5" r="3"/><path d="M31 30V14l5-4 5 4v16"/><rect x="15" y="10" width="14" height="12"/><path d="M22 10v12M15 16h14"/></svg>
    <span>ZUSAMMENARBEIT<br>FÖRDERN</span>
  </div>
  <div class="benefit" style="left:394px">
    <svg width="44" height="32" viewBox="0 0 44 32" fill="none" stroke="#fff" stroke-width="1.3"><circle cx="11" cy="10" r="4"/><circle cx="22" cy="8" r="4"/><circle cx="33" cy="10" r="4"/><path d="M4 30c0-8 14-8 14 0M15 28c0-9 14-9 14 0M26 30c0-8 14-8 14 0"/><rect x="12" y="22" width="20" height="8"/></svg>
    <span>WISSEN FÜR<br>DIE PRAXIS</span>
  </div>
  <div class="benefit" style="left:484px">
    <svg width="44" height="32" viewBox="0 0 44 32" fill="none" stroke="#fff" stroke-width="1.3"><rect x="12" y="2" width="28" height="18"/><circle cx="7" cy="8" r="3"/><path d="M3 24v-9l4-3 8 3"/><circle cx="15" cy="24" r="2.5"/><circle cx="25" cy="24" r="2.5"/><circle cx="35" cy="24" r="2.5"/><path d="M10 31c0-4 10-4 10 0M20 31c0-4 10-4 10 0M30 31c0-4 10-4 10 0"/></svg>
    <span>SEMINARE<br>INHOUSE</span>
  </div>
  <div class="benefit" style="left:571px">
    <svg width="44" height="32" viewBox="0 0 44 32" fill="none" stroke="#fff" stroke-width="1.3"><rect x="10" y="1" width="24" height="12"/><path d="M18 7l3 3 6-6"/><circle cx="13" cy="19" r="4"/><circle cx="31" cy="19" r="4"/><path d="M5 31c0-8 16-8 16 0M23 31c0-8 16-8 16 0"/></svg>
    <span>KONFLIKTE<br>VERMEIDEN</span>
  </div>

  <div class="abs copy closing"><p>Wir haben es uns zur Aufgabe gemacht dieses <span class="accent">Gleichgewicht in Ihren Betriebsrat</span> und damit in Ihr Unternehmen zu bringen. Mit uns an Ihrer Seite gelingt Ihre Betriebsratsarbeit, das bedeutet zufriedene Mitarbeiter und eine zufriedene Führungsetage, <span class="accent">weil alle gemeinsam ihre Ziele erreichen.</span></p></div>

  <div class="rule" style="left:147px;top:415px;width:474px"></div>
  <p class="abs cta">Jetzt informieren unter <b>www.voran-kolleg.example</b></p>
  <div class="abs wordmark front-mark"><i></i>VORAN</div>
</section>

<section class="flyer flyer--back">
  <svg class="layer" width="651" height="459" role="img" aria-label="Foto: lächelnder Seminarleiter am Whiteboard">
    <defs>
      <linearGradient id="trainerTone" x1="0" y1="0" x2="1" y2="1">
        <stop offset="0" stop-color="#f1f2f3"/>
        <stop offset=".55" stop-color="#b9bcc1"/>
        <stop offset="1" stop-color="#6f7a8a"/>
      </linearGradient>
    </defs>
    <polygon points="547,0 651,0 651,459 610,459 439,202" fill="url(#trainerTone)"/>
  </svg>
  <svg class="layer" width="651" height="459" aria-hidden="true">
    <polyline points="542,0 433,202 603,459" fill="none" stroke="var(--black)" stroke-width="4"/>
    <polyline points="533,0 423,202 594,459" fill="none" stroke="var(--red)" stroke-width="5"/>
  </svg>

  <h2 class="abs back-title">UNSERE INHOUSE SEMINARE<em>So einzigartig wie Ihr Betrieb</em></h2>
  <div class="rule" style="left:26px;top:94px;width:411px"></div>

  <div class="abs copy back-p1"><p>Ein Inhouse Seminar bietet vor allem eins: Individualität. <span class="accent">Das bedeutet Sie erhalten ein Seminar ganz auf Ihre Bedürfnisse zugeschnitten.</span></p></div>
  <div class="abs copy back-p2"><p>Sie wollen selbst entscheiden, welche Inhalte behandelt werden? Kein Problem. Wie viel Zeit wollen Sie investieren? Auch das legen Sie fest. Soll es bei Ihnen im Betrieb stattfinden oder doch lieber im Hotel? Bei einem Inhouse-Seminar geben Sie den Ton an … wenn Sie wollen.</p></div>

  <div class="feature" style="top:196px">
    <svg class="marker" width="50" height="26" aria-hidden="true"><polygon points="0,0 36,0 41,12.5 36,25 0,25" fill="var(--navy)"/><polyline points="38,0 45,12.5 38,25" fill="none" stroke="var(--red)" stroke-width="2.5"/></svg>
    <h3 style="left:54px">FLEXIBEL</h3>
    <p style="left:54px">Sie entscheiden über Inhalte, Veranstaltungsort, Teilnehmer und die Dauer.</p>
  </div>
  <div class="feature" style="top:238px">
    <svg class="marker" width="66" height="26" aria-hidden="true"><polygon points="0,0 52,0 57,12.5 52,25 0,25" fill="var(--navy)"/><polyline points="54,0 61,12.5 54,25" fill="none" stroke="var(--red)" stroke-width="2.5"/></svg>
    <h3 style="left:70px">INDIVIDUELL</h3>
    <p style="left:70px">Betriebspezifische Fragen und Themen können gezielt angesprochen werden.</p>
  </div>
  <div class="feature" style="top:278px">
    <svg class="marker" width="82" height="26" aria-hidden="true"><polygon points="0,0 68,0 73,12.5 68,25 0,25" fill="var(--navy)"/><polyline points="70,0 77,12.5 70,25" fill="none" stroke="var(--red)" stroke-width="2.5"/></svg>
    <h3 style="left:85px">KOSTENEFFIZIENT</h3>
    <p style="left:85px">Abrechnung nach Tagen – demnach besonders für größere Teilnehmerzahlen geeignet.</p>
  </div>

  <div class="abs copy back-p3"><p>Kontaktieren Sie uns ganz unverbindlich, damit wir gemeinsam Ihr Seminar zusammenstellen können. <span class="accent">Sie haben dabei die Möglichkeit ein bestehendes Semminar zu wählen, oder die Inhalte selbst zu bestimmen.</span> Steh der Inhalt fest, können Sie entscheiden wo das Semiar stattfinden soll.</p></div>
  <div class="abs copy back-p4"><p>Ist alles geklärt und sind Sie mit allem zufrieden, erteilen Sie uns den verbindlichen Auftrag zur Durchführung Ihres individuellen Inhouse-Seminars. Fragen Sie jetzt unverbindlich an – <span class="accent">www.voran-kolleg.example</span></p></div>

  <div class="rule" style="left:22px;top:420px;width:527px"></div>
  <div class="abs footer">
    <div class="wordmark"><i></i>VORAN</div>
    <small><b>Akademie für betriebliche Fortbildung</b> • www.voran-kolleg.example • info@voran-kolleg.example • 0160 000 00 00 • Musterweg 12 • 10115 Berlin</small>
  </div>
</section>

</body>
</html>
```